automotive repair and collision repair shop card

our company is called K.W Motor service we are a automotive repair company
we also do government inspections. the company information is on the cards. I would like you to use my new logo and create a new card and use the information from my old card. Good Luck!!

Industry/Entity Type

Car Repair

Contact Information for Business Card

Address: #417-10952 58 Ave, Surrey, BC V3X 4K8
Phone:(604) 555-0178
fax 604 555 0193
website www.kwmotorworks.example

Font styles to use
Serif
Sans Serif

Requirements
Must have
• all the information
Should not have
• the owner and there name

```html
<!DOCTYPE html>
<html lang="en">
<head>
<meta charset="utf-8">
<title>K.W Motor service – Business Card</title>
<link href="https://fonts.googleapis.com/css2?family=Lato:wght@400;700&display=swap" rel="stylesheet">
<style>
  :root {
    --backdrop: #3b3430;
    --card: #161616;
    --card-edge: #0c0c0c;
    --text-strong: #b9b9b9;
    --text-soft: #7d7d7d;
    --divider: #3a3a3a;
  }
  html, body {
    margin: 0;
    width: 1200px;
    height: 844px;
    overflow: hidden;
    background: var(--backdrop);
    font-family: "Lato", sans-serif;
  }
  .sheet {
    position: relative;
    width: 1200px;
    height: 844px;
  }
  .card {
    position: absolute;
    top: 272px;
    width: 520px;
    height: 300px;
    background: radial-gradient(ellipse at 40% 35%, #232323 0%, var(--card) 60%, var(--card-edge) 100%);
    box-shadow: 0 6px 18px rgba(0,0,0,.45);
    overflow: hidden;
  }
  .card--info { left: 60px; }
  .card--brand { left: 620px; }

  /* information side */
  .info-brand {
    position: absolute;
    left: 30px;
    top: 0;
    bottom: 0;
    width: 210px;
    display: flex;
    align-items: center;
  }
  .brand-name {
    margin: 0;
    font-size: 20px;
    font-weight: 700;
    color: var(--text-strong);
    letter-spacing: .3px;
    white-space: nowrap;
  }
  .divider {
    position: absolute;
    left: 258px;
    top: 70px;
    width: 1px;
    height: 160px;
    background: var(--divider);
  }
  .contact {
    position: absolute;
    left: 278px;
    top: 82px;
    right: 16px;
  }
  .contact-address,
  .contact-lines {
    margin: 0 0 16px;
    font-size: 13px;
    line-height: 1.5;
    color: var(--text-soft);
    font-style: normal;
  }
  .contact-lines { margin: 0; }

  /* brand side */
  .brand-block {
    position: absolute;
    inset: 0;
    display: flex;
    align-items: center;
    justify-content: center;
  }
  .brand-block .brand-name { font-size: 28px; }
</style>
</head>
<body>
<main class="sheet">

  <section class="card card--info">
    <div class="info-brand">
      <p class="brand-name">K.W Motor service</p>
    </div>
    <div class="divider"></div>
    <div class="contact">
      <address class="contact-address">#417-10952 58 Ave,<br>Surrey, BC V3X 4K8</address>
      <p class="contact-lines">
        T: (604) 555-0178<br>
        F: 604 555 0193<br>
        E: info@kwmotorworks.example<br>
        W: www.kwmotorworks.example
      </p>
    </div>
  </section>

  <section class="card card--brand">
    <div class="brand-block">
      <p class="brand-name">K.W Motor service</p>
    </div>
  </section>

</main>
</body>
</html>
```